Swiftpath STEM by graduating students from college in two years

Based on the logo design, create stationary and business cards for
Dr. Velimir T Osunde, CEO, (703) 482-1630
and Mirela Thorpe, Respresentative, (301) 557-2048
Address: 4417 Marbleton Lane, Faurfax Station, VA 22061
Incorporate elelments of the logo

Target Market(s)

USA

Other font styles liked:
• match with the logo type style

```html
<!DOCTYPE html>
<html lang="en">
<head>
<meta charset="utf-8">
<title>Swiftpath STEM Stationery</title>
<link rel="stylesheet" href="https://fonts.googleapis.com/css2?family=Poppins:wght@400;500;600;700&display=swap">
<style>
:root{
  --navy:#1f2a5c;
  --gold:#f8c22d;
  --ink:#1f2a5c;
  --grey-text:#8a8a8f;
  --bg:#d9dadd;
  --paper:#ffffff;
  --cap:#f1f1f3;
}
*{box-sizing:border-box;margin:0;padding:0}
html,body{width:1200px;height:997px;overflow:hidden}
body{background:var(--bg);font-family:'Poppins',sans-serif;color:var(--ink);position:relative}
.sheet{position:absolute;background:var(--paper);box-shadow:0 6px 14px rgba(0,0,0,.18);overflow:hidden}
.deco{position:absolute;left:0;top:0}
.illustration-area{position:absolute;background:radial-gradient(ellipse at 55% 45%,#eeeef1 0%,#f3f3f5 55%,rgba(255,255,255,0) 100%)}
.brand{display:flex;align-items:center;gap:6px;position:absolute}
.brand-dot{border-radius:50%;background:var(--gold);flex:none}
.brand-name{font-weight:700;color:var(--navy);line-height:1.1}
.phone{display:flex;align-items:center;gap:4px;color:#6c6c72}
.phone-icon{background:var(--gold);border-radius:2px;display:flex;align-items:center;justify-content:center}
.phone-icon svg{display:block}

/* business card front */
.card-front{left:71px;top:213px;width:418px;height:251px}
.card-front .illustration-area{left:186px;top:101px;width:232px;height:150px}
.card-front .person{position:absolute;left:29px}
.card-front .person-name{font-size:13.5px;font-weight:700;text-transform:uppercase;letter-spacing:.1px;line-height:1.1}
.card-front .person-role{font-size:9.5px;font-weight:500;line-height:1.35}
.card-front .phone{font-size:11px;margin-top:5px}
.card-front .phone-icon{width:12px;height:12px}
.card-front .address{position:absolute;left:29px;top:178px;font-size:9.5px;color:#55555b;line-height:1.15}
.card-front .address-label{font-size:11.5px;font-weight:700;color:var(--navy)}
.card-front .brand{left:286px;top:58px}
.card-front .brand-dot{width:18px;height:18px}
.card-front .brand-name{font-size:12px}

/* business card back */
.card-back{left:71px;top:533px;width:419px;height:251px;background:var(--navy)}
.card-back .rule{position:absolute;left:0;right:0;top:124px;height:2px;background:var(--gold)}
.card-back .seal{position:absolute;left:148px;top:64px;width:122px;height:122px;border-radius:50%;background:var(--paper);display:flex;align-items:center;justify-content:center;text-align:center;font-size:14px;font-weight:700;color:var(--navy);line-height:1.15}

/* letterhead */
.letterhead{left:570px;top:102px;width:560px;height:792px}
.letterhead .illustration-area{left:290px;top:612px;width:270px;height:180px}
.letterhead .brand{left:52px;top:62px}
.letterhead .brand-dot{width:22px;height:22px}
.letterhead .brand-name{font-size:12px}
.contact-col{position:absolute;top:64px}
.contact-col .col-name{font-size:11px;font-weight:700;line-height:1.2}
.contact-col .col-role{font-size:7.5px;font-weight:500;line-height:1.3}
.contact-col .phone{font-size:8.5px;margin-top:5px}
.contact-col .phone-icon{width:10px;height:10px}
.contact-col .col-address{font-size:8px;color:#55555b;line-height:1.3;margin-top:4px}
.col-divider{position:absolute;top:57px;width:1px;height:53px;background:var(--gold)}
.recipient{position:absolute;left:44px;top:220px;color:var(--grey-text);font-size:10px;line-height:1.75}
.recipient-name{font-size:14px;font-weight:500;color:var(--navy);letter-spacing:.5px;margin-bottom:8px}
.recipient .addr{line-height:1.3;margin-top:2px}
.letter-date{position:absolute;right:41px;top:304px;font-size:12px;font-weight:500;color:var(--grey-text)}
.letter-body{position:absolute;left:44px;top:336px;width:475px;font-size:10.8px;line-height:17px;color:var(--grey-text);text-align:justify;hyphens:auto}
.letter-body p+p{margin-top:17px}
.signoff{position:absolute;left:44px;top:566px;font-size:13px;font-weight:500;color:#222}
.signature{position:absolute;left:48px;top:596px;width:82px;height:28px;background:linear-gradient(90deg,#e8e8ea,#f4f4f6);border-radius:3px}
</style>
</head>
<body>

<section class="sheet card-front" aria-label="Business card front">
  <div class="illustration-area" role="img" aria-label="Faint graduation cap illustration"></div>
  <svg class="deco" width="418" height="251" viewBox="0 0 418 251">
    <polygon points="0,241 303,241 319,251 0,251" fill="var(--navy)"/>
    <polygon points="418,168 391,183 391,225 338,251 418,251" fill="var(--gold)"/>
  </svg>
  <div class="brand">
    <span class="brand-dot"></span>
    <span class="brand-name">Swiftpath<br>STEM</span>
  </div>
  <div class="person" style="top:43px">
    <div class="person-name">Dr. Velimir T Osunde</div>
    <div class="person-role">CEO</div>
    <div class="phone"><span class="phone-icon"><svg width="8" height="8" viewBox="0 0 24 24"><path d="M6.6 10.8a15 15 0 0 0 6.6 6.6l2.2-2.2c.3-.3.7-.4 1-.2 1.1.4 2.3.6 3.6.6.6 0 1 .4 1 1V20c0 .6-.4 1-1 1A17 17 0 0 1 3 4c0-.6.4-1 1-1h3.5c.6 0 1 .4 1 1 0 1.3.2 2.5.6 3.6.1.3 0 .7-.2 1z" fill="var(--navy)"/></svg></span>(703) 482-1630</div>
  </div>
  <div class="person" style="top:113px">
    <div class="person-name">Mirela Thorpe</div>
    <div class="person-role">Respresentative</div>
    <div class="phone"><span class="phone-icon"><svg width="8" height="8" viewBox="0 0 24 24"><path d="M6.6 10.8a15 15 0 0 0 6.6 6.6l2.2-2.2c.3-.3.7-.4 1-.2 1.1.4 2.3.6 3.6.6.6 0 1 .4 1 1V20c0 .6-.4 1-1 1A17 17 0 0 1 3 4c0-.6.4-1 1-1h3.5c.6 0 1 .4 1 1 0 1.3.2 2.5.6 3.6.1.3 0 .7-.2 1z" fill="var(--navy)"/></svg></span>(301) 557-2048</div>
  </div>
  <div class="address">
    <div class="address-label">Address:</div>
    4417 Marbleton Lane, Faurfax<br>Station, VA 22061
  </div>
</section>

<section class="sheet card-back" aria-label="Business card back">
  <div class="rule"></div>
  <div class="seal">Swiftpath<br>STEM</div>
</section>

<section class="sheet letterhead" aria-label="Letterhead">
  <div class="illustration-area" role="img" aria-label="Faint graduation cap illustration"></div>
  <svg class="deco" width="560" height="792" viewBox="0 0 560 792">
    <path d="M0 49 L43 49 Q28 84 43 118 L0 118 Z" fill="var(--navy)"/>
    <polygon points="0,781 390,781 408,792 0,792" fill="var(--navy)"/>
    <polygon points="560,700 520,722 520,760 465,792 560,792" fill="var(--gold)"/>
  </svg>
  <div class="brand">
    <span class="brand-dot"></span>
    <span class="brand-name">Swiftpath<br>STEM</span>
  </div>
  <div class="contact-col" style="left:167px">
    <div class="col-name">Dr. Velimir T Osunde</div>
    <div class="col-role">CEO</div>
    <div class="phone"><span class="phone-icon"><svg width="7" height="7" viewBox="0 0 24 24"><path d="M6.6 10.8a15 15 0 0 0 6.6 6.6l2.2-2.2c.3-.3.7-.4 1-.2 1.1.4 2.3.6 3.6.6.6 0 1 .4 1 1V20c0 .6-.4 1-1 1A17 17 0 0 1 3 4c0-.6.4-1 1-1h3.5c.6 0 1 .4 1 1 0 1.3.2 2.5.6 3.6.1.3 0 .7-.2 1z" fill="var(--navy)"/></svg></span>(703) 482-1630</div>
  </div>
  <div class="col-divider" style="left:288px"></div>
  <div class="contact-col" style="left:304px">
    <div class="col-name">Mirela Thorpe</div>
    <div class="col-role">Respresentative</div>
    <div class="phone"><span class="phone-icon"><svg width="7" height="7" viewBox="0 0 24 24"><path d="M6.6 10.8a15 15 0 0 0 6.6 6.6l2.2-2.2c.3-.3.7-.4 1-.2 1.1.4 2.3.6 3.6.6.6 0 1 .4 1 1V20c0 .6-.4 1-1 1A17 17 0 0 1 3 4c0-.6.4-1 1-1h3.5c.6 0 1 .4 1 1 0 1.3.2 2.5.6 3.6.1.3 0 .7-.2 1z" fill="var(--navy)"/></svg></span>(301) 557-2048</div>
  </div>
  <div class="col-divider" style="left:396px"></div>
  <div class="contact-col" style="left:408px">
    <div class="col-name">Address:</div>
    <div class="col-address">4417 Marbleton Lane, Faurfax<br>Station, VA 22061</div>
  </div>

  <div class="recipient">
    <div class="recipient-name">MR. ALDOUS PENRAKE</div>
    <div>0144-208-367</div>
    <div>hello@swiftpathmail.com</div>
    <div class="addr">5820 Harrowgate Ln. Suite<br>210 Dallas, TX 75201</div>
  </div>
  <div class="letter-date">12 December, 2025</div>

  <div class="letter-body">
    <p>Lorem ipsum dolor sit amet, consectetuer adipiscing elit, sed diam nonummy nibh euismod tincidunt ut laoreet dolore magna aliquam erat volutpat. Ut wisi enim ad minim veniam, quis nostrud exerci tation ullamcorper suscipit lobortis nisl ut aliquip ex ea commodo consequat. Duis autem vel eum iriure dolor in hendrerit in vulputate velit esse molestie consequat, vel illum dolore eu feugiat nulla facilisis at vero eros et accumsan et iusto odio dignissim qui blandit praesent luptatum zzril delenit augue duis dolore te feugait nulla facilisi.</p>
    <p>Lorem ipsum dolor sit amet, cons ectetuer adipiscing elit, sed diam nonummy nibh euismod tincidunt ut laoreet dolore magna aliquam erat volutpat. Ut wisi enim ad minim veniam, quis nostrud exerci tation ullamcorper suscipit lobortis nisl ut aliquip ex ea commodo consequat.</p>
  </div>
  <div class="signoff">Mr. Aldous Penrake</div>
  <div class="signature" role="img" aria-label="Handwritten signature"></div>
</section>

</body>
</html>
```